I Need a New Design For Existing Wordpress Site

My website is www.fretmorningacademy.example. The purpose is to provide free guitar lessons. Each blog post is a new video lesson embedded from ClipStreamo. The site is also an avenue to sell my ebook.

I need a Wordpress design that is appealing and professional. It should make the user feel as if the site is legitimate and trustworthy. I like the color schemes that use blues, grey,s and white matching my logo.

Examples of website designs I like:
www.strumvelta.example
www.pinehavenworks.example
www.steadyyieldnotes.example

Target Market(s)

15-35 year old males. Rock n roll, country, and pop music

Industry/Entity Type

ClipStreamo

Font styles to use
Sans Serif

Colors
0255a3
0792cd
ffffff
333333

Requirements
Must have
• Modern professional look

```html
<!DOCTYPE html>
<html lang="en">
<head>
<meta charset="utf-8">
<title>Fretmorning Academy – Free Guitar Lessons</title>
<link rel="stylesheet" href="https://fonts.googleapis.com/css2?family=Open+Sans:wght@400;600;700;800&display=swap">
<style>
:root{
  --blue:#0255a3;
  --blue-light:#0792cd;
  --white:#ffffff;
  --dark:#333333;
  --darker:#2b2b2b;
  --grey-bg:#f4f4f4;
  --grey-text:#9a9a9a;
  --grey-mid:#777777;
  --grey-line:#e2e2e2;
}
*{box-sizing:border-box;margin:0;padding:0}
html,body{width:726px;height:1200px;overflow:hidden;background:var(--white)}
body{font-family:"Open Sans",Arial,sans-serif;color:var(--dark);position:relative}
section,header,footer{position:relative;width:726px;overflow:hidden}
.btn{position:absolute;display:flex;align-items:center;justify-content:center;background:var(--blue);color:var(--white);font-weight:700;text-transform:uppercase;font-size:6px;letter-spacing:.3px}
.btn-white{background:var(--white);color:var(--dark)}
.section-title{position:absolute;left:152px;border-left:3px solid var(--blue);padding-left:5px;font-size:12.5px;font-weight:800;color:var(--blue);text-transform:uppercase;line-height:14px}
.section-title::after{content:"";position:absolute;left:5px;right:0;bottom:-3px;height:1px;background:var(--blue-light)}
.section-title.light{color:var(--white)}
.photo{position:absolute;background:linear-gradient(135deg,#6a5a4e,#b9a48e)}

/* header */
.site-header{height:58px;background:var(--white)}
.top-strip{position:absolute;right:0;top:0;width:300px;height:14px;background:#ececec}
.top-link{position:absolute;left:446px;top:3.5px;font-size:5.5px;font-weight:700;color:var(--blue);white-space:nowrap}
.top-cta{position:absolute;left:522px;top:1px;width:56px;height:11px;background:var(--dark);color:var(--white);font-size:5.5px;font-weight:700;display:flex;align-items:center;justify-content:center;white-space:nowrap}
.brand{position:absolute;left:154px;top:13px;display:flex;align-items:center;gap:5px;font-size:11px;font-weight:800;color:var(--dark);line-height:11px;text-transform:uppercase}
.brand-dot{width:14px;height:14px;border-radius:50%;background:var(--blue)}
.contact-line{position:absolute;left:496px;font-size:6px;color:var(--grey-mid);display:flex;align-items:center;gap:3px}
.main-nav{position:absolute;left:148px;top:43px;width:430px;height:14px;background:var(--dark);display:flex}
.main-nav a{color:var(--white);text-decoration:none;font-size:5.5px;font-weight:600;text-transform:uppercase;display:flex;align-items:center;padding:0 15px}
.main-nav a.current{background:var(--blue)}
.social{position:absolute;display:flex;gap:3px}
.social span{width:9px;height:9px;border-radius:50%;background:#8c8c8c}

/* hero */
.hero{height:209px;background:radial-gradient(ellipse 260px 170px at 290px 100px,#0a78d4 0%,#0560ad 45%,#073a6e 100%)}
.hero-title{position:absolute;left:189px;top:52px;color:var(--white);font-size:20px;font-weight:800;line-height:23px;letter-spacing:.8px}
.hero-sub{position:absolute;left:189px;top:101px;color:var(--white);font-size:8.5px;line-height:10px;letter-spacing:.3px;text-transform:uppercase;font-weight:600}
.hero-arrow{position:absolute;top:94px;width:15px;height:15px;border:1px solid var(--white);border-radius:50%;display:flex;align-items:center;justify-content:center}
.book{position:absolute;background:linear-gradient(160deg,#ffffff,#e9e9e9);box-shadow:4px 6px 10px rgba(0,0,0,.35)}
.dots{position:absolute;left:356px;top:195px;display:flex;gap:3px}
.dots span{width:4px;height:4px;border-radius:50%;background:#8fb5da}
.dots span:first-child{background:var(--white)}

/* about */
.about{height:105px;background:var(--grey-bg)}
.about-text{position:absolute;left:152px;top:38px;width:336px;font-size:6px;line-height:12px;color:var(--grey-text)}

/* videos */
.videos{height:186px;background:var(--white)}
.video-item{position:absolute;width:130px;height:36px}
.video-item .photo{left:0;top:0;width:36px;height:34px}
.video-item h3{position:absolute;left:42px;top:0;font-size:6.2px;font-weight:800;color:var(--blue);text-transform:uppercase;white-space:nowrap}
.video-item p{position:absolute;left:42px;top:11px;width:88px;font-size:5.5px;line-height:8px;color:var(--grey-text)}

/* blog */
.blog{height:192px;background:var(--dark)}
.post-card{position:absolute;top:36px;width:96px;height:112px;background:var(--white);padding:3px}
.post-card h3{font-size:5px;line-height:7px;font-weight:800;color:var(--blue);text-transform:uppercase;height:14px;overflow:hidden}
.post-card .photo{position:relative;display:block;width:90px;height:44px;margin-top:4px}
.post-card p{font-size:5px;line-height:6.5px;color:var(--grey-text);margin-top:4px;height:20px;overflow:hidden}
.post-meta{position:absolute;left:3px;bottom:4px;font-size:4.5px;line-height:6px;color:var(--grey-text)}
.post-card .btn{right:3px;bottom:4px;width:44px;height:12px;font-size:5px}

/* ebook */
.ebook{height:222px;background:var(--white)}
.ebook-title{position:absolute;left:152px;top:44px;width:290px;font-size:13px;line-height:15px;font-weight:700;color:var(--grey-text);text-transform:uppercase;white-space:nowrap}
.ebook-text{position:absolute;left:152px;top:98px;width:250px;font-size:5.5px;line-height:10px;color:var(--grey-text)}
.ebook-text p+p{margin-top:2px}

/* newsletter */
.newsletter{height:84px;background:var(--grey-bg)}
.newsletter h2{position:absolute;left:0;width:726px;top:14px;text-align:center;font-size:11px;font-weight:800;color:var(--blue);text-transform:uppercase}
.newsletter-input{position:absolute;left:193px;top:40px;width:267px;height:20px;background:var(--white);font-size:5.5px;color:var(--grey-text);display:flex;align-items:center;padding-left:12px}

/* footer */
.site-footer{height:142px;background:var(--darker)}
.footer-col{position:absolute;top:36px}
.footer-col h4{font-size:6px;font-weight:800;color:var(--white);text-transform:uppercase;margin-bottom:7px}
.footer-col li{list-style:none;font-size:5.5px;line-height:11px;color:var(--grey-text)}
.footer-links{display:grid;grid-template-columns:57px auto}
.footer-brand{position:absolute;left:480px;top:44px;display:flex;align-items:center;gap:5px;font-size:12px;font-weight:800;color:#7a7a7a;text-transform:uppercase;line-height:13px}
.footer-brand .brand-dot{background:#5a5a5a;width:16px;height:16px}
.copyright{position:absolute;left:0;width:726px;top:124px;text-align:center;font-size:5px;color:var(--grey-mid)}
</style>
</head>
<body>

<header class="site-header">
  <div class="top-strip"></div>
  <span class="top-link">DYING TO LEARN GUITAR?</span>
  <span class="top-cta">GET STARTED HERE</span>
  <div class="brand"><span class="brand-dot"></span><span>Fretmorning<br>Academy</span></div>
  <div class="contact-line" style="top:19px">
    <svg width="6" height="6" viewBox="0 0 10 10"><path d="M2 1l2 0 1 2.5-1.3 1a6 6 0 0 0 2.8 2.8l1-1.3L10 7v2c0 .6-.4 1-1 1A9 9 0 0 1 0 2c0-.6.4-1 1-1z" fill="#777"/></svg>123.456.7890</div>
  <div class="contact-line" style="top:29px">
    <svg width="6" height="5" viewBox="0 0 10 8"><rect x=".5" y=".5" width="9" height="7" fill="none" stroke="#777"/><path d="M.5.5l4.5 4 4.5-4" fill="none" stroke="#777"/></svg>contact@fretmorningacademy.example</div>
  <nav class="main-nav">
    <a class="current">Home</a><a>Instructional Videos</a><a>Privacy Policy</a><a>About</a><a>Contact</a><a>Blog</a>
  </nav>
  <div class="social" style="left:530px;top:45px"><span></span><span></span><span></span><span></span></div>
</header>

<section class="hero">
  <span class="hero-arrow" style="left:152px"><svg width="9" height="9" viewBox="0 0 9 9"><path d="M5.5 2L3 4.5 5.5 7" fill="none" stroke="#fff" stroke-width="1.2"/></svg></span>
  <span class="hero-arrow" style="left:558px"><svg width="9" height="9" viewBox="0 0 9 9"><path d="M3.5 2L6 4.5 3.5 7" fill="none" stroke="#fff" stroke-width="1.2"/></svg></span>
  <h1 class="hero-title">LEARNING GUITAR<br>REDEFINED</h1>
  <p class="hero-sub">A simplified metod to help you stop<br>wishing and start playing.</p>
  <span class="btn btn-white" style="left:189px;top:128px;width:83px;height:20px">Get Starting Here</span>
  <div class="book" role="img" aria-label="Starter Strummer ebook cover by Dale Marrow" style="left:400px;top:24px;width:108px;height:172px;transform:rotate(4deg)"></div>
  <div class="dots"><span></span><span></span><span></span></div>
</section>

<section class="about">
  <h2 class="section-title" style="top:14px">About</h2>
  <p class="about-text">Hi, I'm Dale and I'm the one behind Fretmorning Academy. I started playing guitar in my late teens and am self taught for the most part. There are a lot of things I wish someone had shown me early on, and that's why this site exists. Now I can pick up my guitar and play the songs I love whenever I want, and I want the same for you.</p>
  <div class="photo" role="img" aria-label="Portrait photo of the site author" style="left:506px;top:11px;width:66px;height:58px;background:linear-gradient(160deg,#d9d9d9,#a99a8c)"></div>
  <span class="btn" style="left:506px;top:75px;width:66px;height:16px">Read More</span>
</section>

<section class="videos">
  <h2 class="section-title" style="top:21px">Instructional Videos</h2>
  <div class="video-item" style="left:152px;top:54px"><div class="photo" role="img" aria-label="Video still of guitar lesson"></div><h3>The Long Haul Chords</h3><p>One of the greatest rock and roll songs of all time. A true all time favorite.</p></div>
  <div class="video-item" style="left:298px;top:54px"><div class="photo" role="img" aria-label="Video still of guitar lesson"></div><h3>The Delta Man Guitar</h3><p>The Delta Man is a great song for beginners.</p></div>
  <div class="video-item" style="left:437px;top:54px"><div class="photo" role="img" aria-label="Video still of guitar lesson"></div><h3>How to Play Ledge Walker</h3><p>See the video.</p></div>
  <div class="video-item" style="left:152px;top:106px"><div class="photo" role="img" aria-label="Video still of guitar lesson"></div><h3>Carry Me Home Beginner</h3><p>Carry Me Home has easy chords, but there's a lot of pace to it.</p></div>
  <div class="video-item" style="left:298px;top:106px"><div class="photo" role="img" aria-label="Video still of guitar lesson"></div><h3>Leave It Be Video</h3><p>See the video.</p></div>
  <div class="video-item" style="left:437px;top:106px"><div class="photo" role="img" aria-label="Video still of guitar lesson"></div><h3>How to Play Heavy Metal</h3><p>See the video.</p></div>
  <span class="btn" style="left:506px;top:153px;width:66px;height:16px">More Videos</span>
</section>

<section class="blog">
  <h2 class="section-title light" style="top:19px">News From Blog</h2>
  <article class="post-card" style="left:152px"><h3>The Long Haul Chords – The Porchlights Lesson</h3><div class="photo" role="img" aria-label="Guitarist playing acoustic guitar"></div><p>One of the greatest rock and roll songs of all time. A true all time favorite.</p><div class="post-meta">0 Comments<br>1400 Views</div><span class="btn">Read More</span></article>
  <article class="post-card" style="left:260px"><h3>Carry Me Home Lesson – Corrigan – Easy…</h3><div class="photo" role="img" aria-label="Guitarist playing acoustic guitar"></div><p>One of the greatest rock and roll songs of all time. A true all time favorite.</p><div class="post-meta">0 Comments<br>1400 Views</div><span class="btn">Read More</span></article>
  <article class="post-card" style="left:368px"><h3>The Delta Man Lesson – Wade Tillman Jr – Easy…</h3><div class="photo" role="img" aria-label="Guitarist playing acoustic guitar"></div><p>One of the greatest rock and roll songs of all time. A true all time favorite.</p><div class="post-meta">0 Comments<br>1400 Views</div><span class="btn">Read More</span></article>
  <article class="post-card" style="left:476px"><h3>Leave It Be Lesson – The Marlowes – Easy…</h3><div class="photo" role="img" aria-label="Guitarist playing acoustic guitar"></div><p>One of the greatest rock and roll songs of all time. A true all time favorite.</p><div class="post-meta">0 Comments<br>1400 Views</div><span class="btn">Read More</span></article>
  <span class="btn btn-white" style="left:506px;top:160px;width:66px;height:16px">More News</span>
</section>

<section class="ebook">
  <h2 class="section-title" style="top:21px">Dying to Learn Guitar?</h2>
  <h3 class="ebook-title">Introducing the Starter Strummer:<br>The Complete Beginners Guide to<br>Learning Guitar</h3>
  <div class="ebook-text">
    <p>Starter Strummer is a resource that will walk you through the entire process of learning guitar, from buying your first guitar to playing your first songs, even a good start on improvising and playing your own riffs.</p>
    <p>This is not your typical beginner guitar book. It was put together with simplicity and efficiency in mind. It does not use learning methods that actually discourage rather than help beginners. It does not teach you information that is useless to most people who want to learn guitar. Instead it will help you reach your own goals and begin learning songs you want to learn as soon as possible.</p>
  </div>
  <div class="book" role="img" aria-label="Starter Strummer ebook cover by Dale Marrow" style="left:446px;top:16px;width:100px;height:146px;transform:rotate(4deg)"></div>
  <span class="btn" style="left:404px;top:178px;width:144px;height:24px;font-size:9px;font-weight:600">Get Started Here</span>
</section>

<section class="newsletter">
  <h2>Sign Up For Newsletter</h2>
  <div class="newsletter-input">Enter your email</div>
  <span class="btn" style="left:460px;top:40px;width:72px;height:20px">Sign Up Now</span>
</section>

<footer class="site-footer">
  <div class="footer-col" style="left:154px"><h4>Quick Links</h4>
    <ul class="footer-links"><li>Home</li><li>About</li><li>Instructional Videos</li><li>Contact</li><li>Privacy Policy</li><li>Blog</li></ul></div>
  <div class="footer-col" style="left:274px"><h4>Contact Us</h4>
    <ul><li>Address : Complete Address</li><li>Email : contact@fretmorningacademy.example</li><li>Call : 123.456.7890</li></ul></div>
  <div class="footer-col" style="left:382px"><h4>Social Contact</h4>
    <div class="social" style="position:static"><span></span><span></span><span></span><span></span></div></div>
  <div class="footer-brand"><span class="brand-dot"></span><span>Fretmorning<br>Academy</span></div>
  <p class="copyright">2015 © Fretmorning Academy. All Rights Reserved.</p>
</footer>

</body>
</html>
```